Velvet Oaks rebranding my business with a new business card

I have my new logo and now I need a refresher on my business cards. I really want something fun and fresh. I like black background or anything to make the color pop.
Logo
Name: Velvet Oaks
Contact Info as stated below:
Mira Calloway
647-382-9164
Logo
Name: Velvet Oaks
Mira Calloway
647-382-9164
fb.me/VelvetOaksbyMira
Instagram: @VelvetOaksbyMira

Industry/Entity Type

Business

Contact Information for Business Card

double-sided. Logo on one side. Contact info on the other.

Requirements
Must have
• Logo
• Name: Velvet Oaks
• Contact Info as stated below:
• Mira Calloway
• 647-382-9164
• fb.me/VelvetOaksbyMira
• fb.me/VelvetOaksbyMira

```html
<!DOCTYPE html>
<html lang="en">
<head>
<meta charset="utf-8">
<title>Velvet Oaks – Business Card</title>
<link href="https://fonts.googleapis.com/css2?family=Delius&display=swap" rel="stylesheet">
<style>
  :root {
    --backdrop: #e4e4e4;
    --card-white: #fbfbfb;
    --blush: #f4bcc0;
    --blush-light: #f8d3d6;
    --mint: #5cc3ac;
    --ink: #1c1c1c;
    --frame-pink: #e98a98;
    --logo-tone: #e9a7c6;
  }
  * { box-sizing: border-box; margin: 0; padding: 0; }
  html, body {
    width: 1200px; height: 576px; overflow: hidden;
    background: var(--backdrop);
    font-family: "Delius", "Comic Sans MS", sans-serif;
    color: var(--ink);
  }
  .canvas { position: relative; width: 1200px; height: 576px; }

  .card {
    position: absolute; top: 138px;
    width: 484px; height: 294px;
    border-radius: 14px;
    overflow: hidden;
    box-shadow: 0 3px 8px rgba(0,0,0,0.22);
  }

  /* Front: logo side */
  .card-front { left: 82px; background: var(--blush); }
  .front-badge {
    position: absolute; left: 137px; top: 42px;
    width: 210px; height: 210px; border-radius: 50%;
    background: #fff;
    border: 2px solid var(--ink);
    display: flex; align-items: center; justify-content: center;
  }
  .front-badge::before {
    content: ""; position: absolute; inset: 5px;
    border-radius: 50%; border: 2px solid var(--frame-pink);
  }
  .brand-name {
    font-size: 26px; color: var(--ink); text-align: center; line-height: 1.1;
  }

  /* Back: contact side */
  .card-back { left: 602px; width: 482px; height: 292px; background: var(--card-white); }
  .back-waves { position: absolute; inset: 0; }
  .back-logo {
    position: absolute; left: 38px; top: 22px;
    width: 188px; height: 188px;
    display: flex; align-items: center; justify-content: center;
  }
  .contact-name {
    position: absolute; right: 27px; top: 52px;
    font-size: 25px; line-height: 1;
  }
  .contact-title {
    position: absolute; right: 28px; top: 83px;
    font-size: 11px;
  }
  .contact-line {
    position: absolute; right: 24px;
    display: flex; align-items: center; gap: 8px;
    font-size: 18px;
  }
  .contact-phone { top: 220px; }
  .contact-social { top: 247px; }
  .contact-icon {
    width: 19px; height: 19px; border: 1.6px solid var(--ink);
    border-radius: 4px; display: flex; align-items: center; justify-content: center;
  }
</style>
</head>
<body>
<main class="canvas">

  <section class="card card-front" aria-label="Card front">
    <div class="front-badge">
      <span class="brand-name">Velvet Oaks</span>
    </div>
  </section>

  <section class="card card-back" aria-label="Card back">
    <svg class="back-waves" width="482" height="292" viewBox="0 0 482 292" aria-hidden="true">
      <path d="M0,226 C140,262 300,214 482,150 L482,292 L0,292 Z" fill="var(--blush-light)"/>
      <path d="M0,196 C130,238 300,206 482,126 L482,140 C300,218 150,252 0,218 Z" fill="var(--mint)"/>
      <path d="M40,248 C160,262 260,240 360,198 C270,250 160,270 40,248 Z" fill="var(--mint)"/>
    </svg>

    <div class="back-logo">
      <span class="brand-name">Velvet Oaks</span>
    </div>

    <h1 class="contact-name">Mira Calloway</h1>
    <p class="contact-title">Managing Director</p>

    <p class="contact-line contact-phone">
      647-382-9164
      <span class="contact-icon">
        <svg width="11" height="11" viewBox="0 0 24 24" aria-hidden="true">
          <path d="M6.6 10.8a15 15 0 0 0 6.6 6.6l2.2-2.2c.3-.3.7-.4 1-.2 1.1.4 2.3.6 3.6.6.6 0 1 .4 1 1V20c0 .6-.4 1-1 1C10.6 21 3 13.4 3 4c0-.6.4-1 1-1h3.5c.6 0 1 .4 1 1 0 1.3.2 2.5.6 3.6.1.3 0 .7-.2 1z" fill="var(--ink)"/>
        </svg>
      </span>
    </p>
    <p class="contact-line contact-social">
      VelvetOaksbyMira
      <span class="contact-icon" aria-hidden="true"></span>
    </p>
  </section>

</main>
</body>
</html>
```